Eye Catching Business Card for Optometrist

We've recently refreshed our logo and now we need a fresh and bold look for our business cards. We provide progressive ways to improve people's vision and protect their eye health.

Use our new logo as guidance into the colors to use. As far as style goes, I love how bold and eye catching the card is for Lanternfly Studio. Feel free to use your creative judgement.

Tagline: "Sharper sight for every season."

pertinent info to include:

Dr. Martin Sowerby
Optometrist

2857 Bramwell Ridge Blvd #217
Alderbrook, KS 66021
(555) 382-7190

marty@brightlenshomeoptics.example
www.brightlenshomeoptics.example

```html
<!DOCTYPE html>
<html lang="en">
<head>
<meta charset="utf-8">
<title>Dr. Martin Sowerby – Business Card</title>
<link href="https://fonts.googleapis.com/css2?family=Didact+Gothic&family=Open+Sans:wght@300;400;600;700&display=swap" rel="stylesheet">
<style>
  :root {
    --crimson: #a31422;
    --espresso: #53453a;
    --name-brown: #4e4035;
    --tagline-grey: #858585;
    --paper: #ffffff;
    --frame-line: #8a8a8a;
    --haze: #eeeeee;
  }
  * { box-sizing: border-box; margin: 0; padding: 0; }
  html, body { width: 1200px; height: 1000px; overflow: hidden; background: var(--paper); }
  .canvas {
    position: relative; width: 1200px; height: 1000px;
    border: 2px solid #555; background: var(--paper); overflow: hidden;
  }
  .accent-bar { position: absolute; background: var(--crimson); }
  .accent-bar--top { right: 0; top: 0; width: 31px; height: 186px; }
  .accent-bar--bottom { left: 0; bottom: 0; width: 32px; height: 182px; }

  .card {
    position: absolute; left: 235px; top: 276px; width: 770px; height: 469px;
    border: 1px solid var(--frame-line); background: var(--paper); overflow: hidden;
    font-family: Arial, "Open Sans", sans-serif;
  }
  .card__texture {
    position: absolute; left: 40px; top: 0; width: 730px; height: 420px;
    background: radial-gradient(ellipse at 70% 40%, var(--haze) 0%, rgba(238,238,238,0.4) 45%, rgba(255,255,255,0) 75%);
  }
  .card__name {
    position: absolute; left: 51px; top: 40px; white-space: nowrap;
    font-family: "Didact Gothic", "Open Sans", sans-serif; font-weight: 700;
    font-size: 28px; letter-spacing: 0.6px; word-spacing: -3px; color: var(--name-brown);
    -webkit-text-stroke: 0.8px var(--name-brown);
  }
  .card__title { position: absolute; left: 52px; top: 76px; font-size: 21px; color: var(--crimson); }
  .card__tagline {
    position: absolute; left: 251px; top: 198px; white-space: nowrap;
    font-family: "Open Sans", sans-serif; font-weight: 300; font-size: 32px; color: var(--tagline-grey);
  }
  .band { position: absolute; left: 0; width: 770px; background: var(--crimson); }
  .band--phone { top: 254px; height: 29px; }
  .band--mail { top: 291px; height: 31px; }
  .band--web { top: 330px; height: 32px; }

  .brand-panel {
    position: absolute; left: 47px; top: 194px; width: 192px; height: 194px;
    background: var(--paper); display: flex; flex-direction: column;
    align-items: center; justify-content: center; gap: 16px;
  }
  .brand-panel__square { width: 52px; height: 52px; background: var(--crimson); }
  .brand-panel__name {
    font-family: "Open Sans", sans-serif; font-weight: 700; font-size: 20px;
    line-height: 1.15; color: var(--crimson); text-align: center; text-transform: uppercase;
  }

  .contact {
    position: absolute; left: 264px; display: flex; align-items: center;
    color: var(--paper); font-size: 22px; line-height: 1; white-space: nowrap;
  }
  .contact svg { width: 18px; height: 18px; margin-right: 22px; flex: none; }
  .contact--phone { top: 257px; }
  .contact--mail { top: 295px; }
  .contact--web { top: 334px; }

  .address-bar {
    position: absolute; left: 0; bottom: 0; width: 770px; height: 56px;
    background: var(--espresso); display: flex; align-items: center;
    padding-left: 79px; color: var(--paper); font-size: 22px; white-space: nowrap;
  }
  .address-bar svg { width: 16px; height: 22px; margin-right: 26px; flex: none; }
</style>
</head>
<body>
<div class="canvas">
  <div class="accent-bar accent-bar--top"></div>
  <div class="accent-bar accent-bar--bottom"></div>

  <section class="card">
    <div class="card__texture" role="img" aria-label="Faint grey halftone dot texture"></div>
    <h1 class="card__name">DR. MARTIN SOWERBY</h1>
    <p class="card__title">Optometrist</p>
    <p class="card__tagline">Sharper sight for every season</p>

    <div class="band band--phone"></div>
    <div class="band band--mail"></div>
    <div class="band band--web"></div>

    <div class="brand-panel">
      <div class="brand-panel__square"></div>
      <div class="brand-panel__name">Bright Lens<br>Home Optics</div>
    </div>

    <div class="contact contact--phone">
      <svg viewBox="0 0 24 24" aria-hidden="true"><path fill="#fff" d="M6.6 2.5l3 3.2-2 2.4c1.2 2.7 3.4 5 6.2 6.3l2.3-2 3.3 3-1.7 3.6C9.8 19.4 4.3 13.6 3.2 4.3z"/></svg>
      <span>(555) 382-7190</span>
    </div>
    <div class="contact contact--mail">
      <svg viewBox="0 0 24 24" aria-hidden="true"><rect x="2" y="5" width="20" height="14" fill="none" stroke="#fff" stroke-width="2"/><path d="M2 5l10 8 10-8M2 19l7-7M22 19l-7-7" fill="none" stroke="#fff" stroke-width="1.6"/></svg>
      <span>marty@brightlenshomeoptics.example</span>
    </div>
    <div class="contact contact--web">
      <svg viewBox="0 0 24 24" aria-hidden="true"><g fill="none" stroke="#fff" stroke-width="1.6"><circle cx="12" cy="12" r="10"/><ellipse cx="12" cy="12" rx="4.5" ry="10"/><path d="M2 12h20M4 6.5h16M4 17.5h16"/></g></svg>
      <span>www.brightlenshomeoptics.example</span>
    </div>

    <div class="address-bar">
      <svg viewBox="0 0 16 22" aria-hidden="true"><path fill="#fff" d="M8 0a8 8 0 0 0-8 8c0 6 8 14 8 14s8-8 8-14a8 8 0 0 0-8-8zm0 11.5a3.5 3.5 0 1 1 0-7 3.5 3.5 0 0 1 0 7z"/></svg>
      <span>2857 Bramwell Ridge Blvd #217 Alderbrook, KS 66021</span>
    </div>
  </section>
</div>
</body>
</html>
```